Design a (20.4 x 10.14) Banner that says - Keep Hope Rising From Harvest Crown TV Family

We want a design (20.4 x 10.14) with the words 'Keep Hope Rising' as the main text and 'From Harvest Crown TV Family' underneath. For 'Harvest Crown TV', we'd like you to use the logo which can be found in the image attached.

The image attached is just an example but please let your creative juices flow!

Target Market(s)

Christian

Industry/Entity Type

Christian

Requirements
Must have
• Must have the words 'Keep Hope Rising' and 'From Harvest Crown TV Family'.

```html
<!DOCTYPE html>
<html lang="en">
<head>
<meta charset="utf-8">
<title>Keep Hope Rising – Harvest Crown TV Family</title>
<link rel="stylesheet" href="https://fonts.googleapis.com/css2?family=Great+Vibes&family=Montserrat:wght@400;500;700&display=swap">
<style>
  :root {
    --cyan-light: #7ff0f7;
    --cyan: #2fd3e8;
    --cyan-deep: #10bcd9;
    --photo-light: #aac4dc;
    --photo-mid: #6f8fb4;
    --photo-dark: #3d5a86;
    --white: #ffffff;
  }
  * { margin: 0; padding: 0; box-sizing: border-box; }
  html, body { width: 1200px; height: 596px; overflow: hidden; }
  body { font-family: "Montserrat", sans-serif; }

  .banner {
    position: relative;
    width: 1200px;
    height: 596px;
    overflow: hidden;
    background: linear-gradient(120deg, var(--cyan-deep) 0%, var(--cyan) 45%, var(--cyan-light) 100%);
  }

  .banner__photo {
    position: absolute;
    inset: 0;
    width: 1200px;
    height: 596px;
  }

  .headline__script {
    position: absolute;
    left: 176px;
    top: 168px;
    font-family: "Great Vibes", cursive;
    font-weight: 400;
    font-size: 104px;
    line-height: 1;
    color: var(--cyan);
  }
  .headline__main {
    position: absolute;
    left: 244px;
    top: 262px;
    display: flex;
    align-items: center;
    font-weight: 500;
    font-size: 92px;
    line-height: 1;
    white-space: nowrap;
  }
  .headline__hope {
    color: var(--white);
    letter-spacing: 0.07em;
  }
  .headline__rising {
    letter-spacing: 0.07em;
    background: linear-gradient(90deg, var(--cyan-light), var(--cyan) 60%, var(--cyan-light));
    -webkit-background-clip: text;
    background-clip: text;
    color: transparent;
  }
  .headline__arrows { margin-left: 2px; width: 70px; height: 60px; }

  .signoff {
    position: absolute;
    left: 600px;
    top: 382px;
    transform: translateX(-50%);
    display: flex;
    flex-direction: column;
    align-items: center;
    color: var(--white);
    font-weight: 700;
    white-space: nowrap;
  }
  .signoff__from {
    font-size: 24px;
    letter-spacing: 0.1em;
    line-height: 1.1;
  }
  .signoff__name {
    font-size: 38px;
    line-height: 1.2;
    margin: 2px 0 0;
  }
  .signoff__family {
    font-size: 16px;
    letter-spacing: 0.12em;
    line-height: 1.2;
  }
</style>
</head>
<body>
<main class="banner">
  <svg class="banner__photo" viewBox="0 0 1000 497" preserveAspectRatio="none" role="img" aria-label="Blue-toned photograph of a shepherd cradling a white lamb in their arms">
    <defs>
      <linearGradient id="photoTone" x1="0" y1="0" x2="1" y2="1">
        <stop offset="0" stop-color="var(--photo-dark)"/>
        <stop offset="0.5" stop-color="var(--photo-mid)"/>
        <stop offset="0.8" stop-color="var(--photo-light)"/>
        <stop offset="1" stop-color="var(--photo-mid)"/>
      </linearGradient>
    </defs>
    <path d="M300,0 L965,0 C990,160 885,340 690,497 L0,497 L0,235 C80,125 180,45 300,0 Z" fill="url(#photoTone)"/>
  </svg>

  <h1 class="headline">
    <span class="headline__script">Keep</span>
    <span class="headline__main">
      <span class="headline__hope">HOPE</span>
      <span class="headline__rising">RISING</span>
      <svg class="headline__arrows" viewBox="0 0 70 60" aria-hidden="true">
        <polyline points="8,10 28,30 8,50" fill="none" stroke="#bfeefb" stroke-width="9" opacity="0.75"/>
        <polyline points="30,10 50,30 30,50" fill="none" stroke="#d9f6fd" stroke-width="9" opacity="0.55"/>
      </svg>
    </span>
  </h1>

  <div class="signoff">
    <span class="signoff__from">FROM</span>
    <span class="signoff__name">Harvest Crown TV</span>
    <span class="signoff__family">FAMILY</span>
  </div>
</main>
</body>
</html>
```